electrical company- Company name- Voltmark Trades, slogan- All installations and servicingcolours to stick roughly with logo- greys, blues, black, white. simple yet effective- logo to stand out and attention to name also (gareth). Modern design.

Industry/Entity Type

Business

Contact Information for Business Card

gareth WilliamsElectrician021 994 306info@voltmarktrades.co.nzwww.voltmarktrades.co.nzPO box 5367Palmerston North, 4472

```html
<!DOCTYPE html>
<html lang="en">
<head>
<meta charset="utf-8">
<title>Voltmark Trades – Business Card</title>
<link rel="stylesheet" href="https://fonts.googleapis.com/css2?family=Source+Sans+3:ital,wght@0,400;0,600;1,400&display=swap">
<style>
  :root {
    --stage: #3a3a3a;
    --brand-blue: #1b90d2;
    --bolt-grey: #767676;
    --paper: #f6f6f6;
    --back-grey: #8b8b8b;
    --pattern-grey: #959595;
    --ink-white: #ffffff;
    --logo-dark: #555555;
  }
  * { margin: 0; padding: 0; box-sizing: border-box; }
  html, body {
    width: 1200px; height: 750px; overflow: hidden;
    background: var(--stage);
    font-family: "Source Sans 3", "Myriad Pro", sans-serif;
  }
  .stage { position: relative; width: 1200px; height: 750px; }
  .card {
    position: absolute; top: 227px;
    width: 520px; height: 296px; overflow: hidden;
  }
  .card--front { left: 60px; background: var(--paper); }
  .card--back { left: 620px; background: var(--back-grey); }
  .card__shapes { position: absolute; inset: 0; width: 100%; height: 100%; display: block; }

  .contact { position: absolute; left: 35px; top: 70px; color: var(--ink-white); }
  .contact__name { font-size: 18.5px; font-weight: 600; line-height: 1.1; }
  .contact__role { font-size: 13.5px; font-weight: 400; margin-top: 2px; }
  .contact__address { font-size: 12px; line-height: 15.5px; margin-top: 19px; font-style: normal; }
  .contact__list { list-style: none; margin-top: 11px; font-size: 11px; }
  .contact__item { display: flex; align-items: center; gap: 6px; height: 20px; }
  .contact__icon { width: 13px; height: 13px; flex: none; }

  .brand {
    position: absolute; left: 300px; top: 160px; transform: translateX(-50%);
    display: flex; align-items: center; gap: 9px; white-space: nowrap;
  }
  .card--front .brand { left: 400px; }
  .brand__mark { width: 16px; height: 16px; background: var(--brand-blue); }
  .brand__name { font-size: 25px; font-weight: 600; color: var(--brand-blue); letter-spacing: 0.5px; }

  .pattern { position: absolute; inset: 0; background: var(--pattern-grey); opacity: 0.55; }
  .back-brand {
    position: absolute; right: 36px; top: 196px;
    display: flex; align-items: center; gap: 8px;
  }
  .back-brand__mark { width: 14px; height: 14px; background: var(--ink-white); }
  .back-brand__name { font-size: 21px; font-weight: 600; color: var(--ink-white); }
  .back-url {
    position: absolute; right: 36px; top: 254px;
    font-size: 12px; font-style: italic; color: var(--ink-white);
  }
</style>
</head>
<body>
<main class="stage">

  <section class="card card--front" aria-label="Business card front">
    <svg class="card__shapes" viewBox="0 0 576 328" preserveAspectRatio="none" aria-hidden="true">
      <polygon fill="var(--bolt-grey)"
        points="277,0 305,98 262,95 305,212 266,212 297,328 290,328 262,212 300,212 258,95 300,95 277,0"/>
      <polygon fill="var(--bolt-grey)"
        points="277,0 287,0 312,98 270,98 312,215 273,215 300,328 290,328 266,212 305,212 262,95 305,98"/>
      <polygon fill="var(--brand-blue)"
        points="0,0 277,0 300,95 258,95 300,212 262,212 290,328 0,328"/>
    </svg>

    <div class="contact">
      <h1 class="contact__name">Gareth Pemberly</h1>
      <p class="contact__role">Electrician</p>
      <address class="contact__address">PO box 8142<br>Palmerston North, 4472</address>
      <ul class="contact__list">
        <li class="contact__item">
          <svg class="contact__icon" viewBox="0 0 16 16" aria-hidden="true"><path fill="#fff" d="M3.2 1.2 5.6 1l1.3 3.4-1.6 1.1c.8 1.8 2.2 3.3 4.1 4.3l1.2-1.6 3.4 1.4-.3 2.5c-.2.9-1 1.4-1.9 1.3C6.3 12.8 2.6 9 2 3.4c-.1-.9.4-1.8 1.2-2.2z"/></svg>
          021 573 814
        </li>
        <li class="contact__item">
          <svg class="contact__icon" viewBox="0 0 16 16" aria-hidden="true"><rect x="1" y="3.5" width="14" height="9" fill="#fff"/><path d="M1.5 4 8 9l6.5-5" fill="none" stroke="var(--brand-blue)" stroke-width="1.2"/></svg>
          info@voltmarktrades-example.co.nz
        </li>
        <li class="contact__item">
          <svg class="contact__icon" viewBox="0 0 16 16" aria-hidden="true"><circle cx="8" cy="8" r="7" fill="#fff"/><path d="M5 3.5c1.5 1 .5 2.5 2 3s.5 2-1 2.5S4 11 5 12.5M10 4c-1 1 0 2 1.5 2.5M12 10c-1 0-2 .5-2 2" fill="none" stroke="var(--brand-blue)" stroke-width="1.3"/></svg>
          www.voltmarktrades-example.co.nz
        </li>
      </ul>
    </div>

    <div class="brand">
      <span class="brand__mark" aria-hidden="true"></span>
      <span class="brand__name">Voltmark Trades</span>
    </div>
  </section>

  <section class="card card--back" aria-label="Business card back">
    <div class="pattern" role="img" aria-label="Faint repeating brand pattern covering the card"></div>
    <div class="back-brand">
      <span class="back-brand__mark" aria-hidden="true"></span>
      <span class="back-brand__name">Voltmark Trades</span>
    </div>
    <p class="back-url">www.voltmarktrades-example.co.nz</p>
  </section>

</main>
</body>
</html>
```